Energy Healing for pregnant women postcard

I am an intuitive energy healer specializing in the care of pregnant women and their babies. I have an existing logo that is attached that should be placed on the card,sizing is at your discretion, recolor as needed. The message of the card should be one that conveys tranquility, growth, life and light. Images of pregnancy and motherhood could also fit well on the card, but that is not required if the preceding messages can be conveyed through other imagery. Also on the card, the following should appear: (company name and tag line)Positivity & JoyHealing the mind, body, spirit and soul with Energy provided to all living things by the Universe. Space should be left for my name and credentials on the front, while the address space on the back will be used for more contact information. Opposite the address block on the back, please leave room for a text box that will include benefits of the services. About 2"x3" should suffice.

Target Market(s)

Pregnant women and newly post-partum women

Industry/Entity Type

Health And Wellness

Font styles to use
Script

Colors
b05ba4
b768aa
d3a5cc
ecdaeb
e7f5f8
cfdeed
cee9f5
85cae6

Requirements
Must have
• Company logo. Company name. Tag line. Individual name and certifications
Nice to have
• Pictures or images that convey peace, tranquility healing and growth.
Should not have
• Anything harsh.

```html
<!DOCTYPE html>
<html lang="en">
<head>
<meta charset="utf-8">
<title>Harbor &amp; Wren – Energy Healing Postcard</title>
<link rel="stylesheet" href="https://fonts.googleapis.com/css2?family=Lato:ital,wght@0,400;0,700;1,400&family=Merienda:wght@700;900&display=swap">
<style>
  :root {
    --stage: #a08a76;
    --magenta: #b8308f;
    --magenta-deep: #9c2479;
    --sky: #2fa6dc;
    --sky-light: #5fc3ec;
    --ink: #3a3f47;
    --paper: #ffffff;
    --mist: #f1f1f3;
    --sage: #8fae94;
    --stamp: #c9c9cb;
  }
  * { margin: 0; padding: 0; box-sizing: border-box; }
  html, body { width: 825px; height: 1200px; overflow: hidden; }
  body { background: var(--stage); font-family: "Lato", sans-serif; position: relative; }

  .postcard { position: absolute; left: 97px; width: 633px; height: 490px; background: var(--paper); overflow: hidden; box-shadow: 0 4px 14px rgba(0,0,0,.25); }
  .postcard--front { top: 78px; }
  .postcard--back { top: 612px; }
  .postcard__art { position: absolute; inset: 0; }

  .tagline { position: absolute; font-family: "Merienda", cursive; font-weight: 700; line-height: 1.45; white-space: nowrap; }
  .front-tagline { top: 12px; right: 20px; text-align: right; font-size: 15.5px; color: var(--paper); }
  .back-tagline { top: 222px; left: 0; width: 290px; text-align: center; font-size: 13px; color: var(--paper); line-height: 1.5; }
  .back-tagline .dark { color: var(--ink); }

  .slogan { position: absolute; top: 272px; left: 274px; font-family: "Merienda", cursive; font-weight: 700; font-size: 18.5px; color: var(--sky-light); line-height: 36px; white-space: nowrap; }

  .practitioner { position: absolute; left: 32px; top: 310px; color: var(--paper); }
  .practitioner__name { font-size: 19px; font-weight: 700; margin-bottom: 6px; }
  .practitioner__creds { font-style: italic; font-size: 13px; line-height: 20.5px; }

  .brand { position: absolute; font-family: "Lato", sans-serif; font-weight: 700; color: var(--sage); display: flex; align-items: center; gap: 5px; white-space: nowrap; }
  .brand::before { content: ""; width: 9px; height: 9px; border-radius: 50%; background: var(--sage); }
  .front-brand { left: 272px; top: 360px; font-size: 14px; }
  .back-brand { left: 10px; top: 40px; font-size: 12.5px; }

  .intro { position: absolute; left: 390px; top: 335px; width: 222px; font-style: italic; font-size: 10.5px; line-height: 15.5px; color: var(--ink); text-align: justify; text-align-last: right; }

  .benefits { position: absolute; left: 22px; top: 322px; list-style: none; color: var(--paper); font-style: italic; font-size: 14px; line-height: 19.5px; }
  .benefits li::before { content: "•"; margin-right: 7px; font-style: normal; }

  .contact { position: absolute; left: 0; right: 0; bottom: 0; height: 48px; text-align: center; line-height: 48px; color: var(--paper); font-size: 14px; letter-spacing: 1.3px; white-space: nowrap; }
</style>
</head>
<body>

<section class="postcard postcard--front">
  <svg class="postcard__art" width="633" height="490" viewBox="0 0 633 490">
    <defs>
      <linearGradient id="front-sky" x1="0" x2="1"><stop offset="0" stop-color="#2b9ed8"/><stop offset="1" stop-color="#62c6ee"/></linearGradient>
      <linearGradient id="front-pink" x1="0" x2="1"><stop offset="0" stop-color="#b8308f"/><stop offset="1" stop-color="#d9459f"/></linearGradient>
      <radialGradient id="mother-tone" cx=".5" cy=".6" r=".7"><stop offset="0" stop-color="#eccfbb"/><stop offset=".5" stop-color="#efe2d8"/><stop offset="1" stop-color="#fbfaf9"/></radialGradient>
      <linearGradient id="child-tone" x1="0" x2="1"><stop offset="0" stop-color="#ececed"/><stop offset=".45" stop-color="#e8cdbd"/><stop offset=".75" stop-color="#e3bfa6"/><stop offset="1" stop-color="#f3f1f0"/></linearGradient>
    </defs>
    <rect width="633" height="490" fill="var(--mist)"/>
    <path d="M245 0 H633 V100 H262 C258 60 252 28 245 0 Z" fill="url(#front-sky)"/>
    <rect x="262" y="100" width="371" height="5" fill="var(--magenta)"/>
    <path role="img" aria-label="Photo of a small girl kissing her mother's pregnant belly" d="M262 105 H633 V252 H265 C266 200 265 150 262 105 Z" fill="url(#child-tone)"/>
    <rect x="262" y="252" width="371" height="4" fill="var(--sky)"/>
    <path d="M0 235 C110 300 240 260 265 120 C262 250 270 370 305 437 H0 Z" fill="url(#front-pink)"/>
    <path d="M265 120 C262 250 270 370 305 437" fill="none" stroke="var(--sky)" stroke-width="4"/>
    <path role="img" aria-label="Photo of a smiling pregnant woman sitting cross-legged, holding her belly" d="M0 0 H250 C262 60 266 110 262 130 C235 255 110 290 0 242 Z" fill="url(#mother-tone)"/>
    <path d="M0 242 C110 290 235 255 262 130" fill="none" stroke="var(--sky)" stroke-width="4"/>
    <rect x="260" y="272" width="354" height="36" rx="18" fill="var(--ink)" stroke="var(--magenta)" stroke-width="3"/>
    <rect x="0" y="435" width="633" height="6" fill="var(--magenta)"/>
    <rect x="0" y="441" width="633" height="49" fill="url(#front-sky)"/>
  </svg>

  <p class="tagline front-tagline">Healing the mind, body, spirit<br>and soul with Energy provided to<br>all living things by the Universe</p>
  <p class="slogan">Spreading growth, life &amp; light</p>

  <div class="practitioner">
    <h1 class="practitioner__name">Maren L. Ashby</h1>
    <p class="practitioner__creds">MSN, RCMT<br>Reiki Master Teacher,<br>Archangelic<br>Light Master Teacher</p>
  </div>

  <p class="brand front-brand">Harbor &amp; Wren</p>
  <p class="intro">Lorem ipsum dolor sit amet, consectetuer adipiscing elit, sed diam nonummy nibh euismod tincidunt ut laoreet dolore magna aliquam erat volutpat.nibhddf dfdf euismod tincidunt ut laoreet dolore magna</p>

  <p class="contact">www.website.com | Mail : email@website.com | Call : 123.456.789</p>
</section>

<section class="postcard postcard--back">
  <svg class="postcard__art" width="633" height="490" viewBox="0 0 633 490">
    <defs>
      <linearGradient id="back-sky" x1="0" x2="1"><stop offset="0" stop-color="#2b9ed8"/><stop offset="1" stop-color="#62c6ee"/></linearGradient>
      <linearGradient id="back-pink" x1="0" x2="1"><stop offset="0" stop-color="#b8308f"/><stop offset="1" stop-color="#d9459f"/></linearGradient>
      <radialGradient id="couple-tone" cx=".6" cy=".6" r=".7"><stop offset="0" stop-color="#e7c8b3"/><stop offset=".55" stop-color="#f0e3da"/><stop offset="1" stop-color="#ffffff"/></radialGradient>
      <radialGradient id="circle-tone" cx=".5" cy=".6" r=".6"><stop offset="0" stop-color="#7f9fd0"/><stop offset=".55" stop-color="#c9d3e6"/><stop offset="1" stop-color="#f4f2f1"/></radialGradient>
      <linearGradient id="faded-tone" x1="0" y1="0" x2="0" y2="1"><stop offset="0" stop-color="#f8f6f5"/><stop offset=".5" stop-color="#f1ece9"/><stop offset="1" stop-color="#f8f8f8"/></linearGradient>
    </defs>
    <rect width="633" height="490" fill="var(--paper)"/>
    <path role="img" aria-label="Faded photo of a pregnant woman sitting and resting her hands on her belly" d="M395 0 H633 V440 H380 C430 330 440 150 395 0 Z" fill="url(#faded-tone)"/>
    <path role="img" aria-label="Photo of a smiling man resting his head against his pregnant partner's belly" d="M118 0 H262 V200 H118 Z" fill="url(#couple-tone)"/>
    <path d="M385 0 C440 130 430 330 360 440" fill="none" stroke="#e3e3e5" stroke-width="14"/>
    <path d="M398 0 C452 130 442 330 372 440" fill="none" stroke="var(--magenta)" stroke-width="6"/>
    <circle cx="330" cy="105" r="79" fill="var(--paper)" stroke="var(--sky)" stroke-width="3"/>
    <circle role="img" aria-label="Photo of a pregnant woman in a blue top relaxing" cx="330" cy="105" r="72" fill="url(#circle-tone)"/>
    <rect x="543" y="24" width="62" height="62" fill="var(--stamp)"/>
    <path d="M0 208 H295 C305 235 307 265 305 297 H0 Z" fill="url(#back-pink)"/>
    <path d="M0 302 H306 C330 350 360 400 400 440 H0 Z" fill="url(#back-sky)"/>
    <rect x="0" y="440" width="633" height="4" fill="var(--sky)"/>
    <rect x="0" y="444" width="633" height="46" fill="url(#back-pink)"/>
  </svg>

  <p class="brand back-brand">Harbor &amp; Wren</p>

  <p class="tagline back-tagline">Healing the mind, body, spirit<br><span class="dark">and soul with Energy provided to</span><br>all living things by the Universe</p>

  <ul class="benefits">
    <li>Deep relaxation &amp; Decrease anxiety</li>
    <li>Decrease stress &amp; Decrease discomforts</li>
    <li>Promote feelings of wellbeing</li>
    <li>Promote balance</li>
    <li>Relieve physical discomforts of pregnancy</li>
  </ul>

  <p class="contact">www.website.com | Mail : email@website.com | Call : 123.456.789</p>
</section>

</body>
</html>
```